Aloe Vera Skin Care Design

Looking to update our 3 Aloe Vera products design, looking for something vibrant and refreshing that you would associate with the skin care product.
A complete front and rear label are required to replace those shown on the attached images, using all text presented in word document. Keep style of 'VARUMEK' the same please.

Current design of 3 products and required text is attached

Colors

Designer to choose colors to be used in the design.

Requirements
Must have
• A complete front and rear label are required to replace those shown on the attached images, using all text presented in word document. Keep style of 'VARUMEK' the same please.

```html
<!DOCTYPE html>
<html lang="en">
<head>
<meta charset="utf-8">
<title>Varumek Aloe Vera Gel – Front and Rear Labels</title>
<link rel="stylesheet" href="https://fonts.googleapis.com/css2?family=Oswald:wght@500;600;700&family=Roboto:wght@400;500;700&family=Encode+Sans+Condensed:wght@400&family=Kaushan+Script&display=swap">
<style>
  :root {
    --page: #ffffff;
    --label-bg: #f8f2f8;
    --forest: #0d4a2b;
    --leaf: #5a9e57;
    --band: #5f9f5a;
    --ink: #111111;
    --white: #ffffff;
    --plant-light: #8fd07a;
    --plant-dark: #1f7a35;
  }
  * { box-sizing: border-box; margin: 0; padding: 0; }
  html, body {
    width: 1200px; height: 1034px; overflow: hidden;
    background: var(--page);
  }
  .sheet { position: relative; width: 1200px; height: 1034px; }

  .label {
    position: absolute; top: 53px; width: 380px; height: 928px;
    background: var(--label-bg);
    border: 2px solid var(--forest);
    border-radius: 190px 190px 0 0 / 162px 162px 0 0;
    overflow: hidden;
  }
  .label--front { left: 190px; }
  .label--rear { left: 630px; }

  .brand {
    position: absolute; left: 0; right: 0; text-align: center;
    font-family: "Roboto", sans-serif; font-weight: 500;
    color: var(--ink); letter-spacing: 1px;
  }
  .label--front .brand { top: 90px; font-size: 57px; }
  .label--rear .brand { top: 54px; font-size: 38px; }

  .title {
    position: absolute; left: 0; right: 0; text-align: center;
    font-family: "Oswald", sans-serif; font-weight: 700; line-height: 1;
  }
  .title__main { top: 282px; font-size: 62px; color: var(--forest); letter-spacing: 2px; }
  .title__sub { top: 346px; font-size: 66px; color: var(--leaf); letter-spacing: 2px; }

  .tagline {
    position: absolute; top: 540px; left: 66px;
    font-family: "Kaushan Script", cursive; font-size: 72px; line-height: 1.2;
    color: var(--forest); white-space: nowrap;
  }
  .rule-dashed {
    position: absolute; left: 0; right: 0; border-top: 2px dashed var(--forest);
  }
  .label--front .rule-dashed { top: 630px; }

  .natural {
    position: absolute; top: 643px; left: 10px; display: flex; align-items: center; gap: 6px;
  }
  .natural__pct {
    background: var(--forest); color: var(--white);
    font-family: "Oswald", sans-serif; font-weight: 600; font-size: 36px;
    line-height: 44px; padding: 0 6px;
  }
  .natural__text { font-family: "Oswald", sans-serif; color: var(--leaf); line-height: 1; }
  .natural__text b { display: block; font-size: 25px; font-weight: 600; letter-spacing: 1px; }
  .natural__text span { display: block; font-size: 15px; font-weight: 500; margin-top: 3px; }

  .rule-solid { position: absolute; left: 0; right: 0; background: var(--forest); }
  .rule-solid--top { top: 697px; height: 3px; }
  .rule-solid--bottom { top: 832px; height: 4px; }

  .band {
    position: absolute; top: 707px; left: 0; right: 0; height: 118px;
    background: var(--band);
  }
  .band__text {
    position: absolute; top: 16px; left: 14px;
    font-family: "Encode Sans Condensed", sans-serif; font-size: 27px;
    line-height: 29px; color: var(--white);
  }
  .plant {
    position: absolute; top: 622px; left: 228px; width: 152px; height: 203px;
    background: linear-gradient(160deg, var(--plant-light), var(--plant-dark));
    border-radius: 60% 40% 0 0;
  }
  .volume {
    position: absolute; top: 862px; left: 0; right: 0; text-align: center;
    font-family: "Roboto", sans-serif; font-size: 36px; color: var(--ink);
  }

  /* rear */
  .label--rear .rule-dashed--upper { top: 131px; left: 58px; right: 52px; }
  .label--rear .rule-dashed--lower { top: 553px; left: 58px; right: 52px; }
  .heading-box {
    position: absolute; top: 135px; left: 58px; width: 268px; height: 38px;
    background: var(--band); color: var(--white); text-align: center;
    font-family: "Oswald", sans-serif; font-weight: 600; font-size: 26px; line-height: 38px;
    letter-spacing: 1px;
  }
  .heading-box--under { top: 173px; height: 0; border-top: 2px dashed var(--forest); background: none; }
  .about {
    position: absolute; top: 184px; left: 0; right: 0; text-align: center;
    font-family: "Roboto", sans-serif; font-size: 20.5px; line-height: 26.4px; color: var(--ink);
    white-space: nowrap;
  }
  .ingredients-tag {
    position: absolute; top: 333px; left: 96px; width: 191px; height: 27px;
    background: var(--forest); color: var(--white); text-align: center;
    font-family: "Roboto", sans-serif; font-weight: 700; font-size: 19px; line-height: 27px;
  }
  .ingredients {
    position: absolute; top: 378px; left: 0; right: 0; text-align: center;
    font-family: "Roboto", sans-serif; font-size: 16.8px; line-height: 21.7px; color: var(--ink);
    white-space: nowrap;
  }
  .distributor {
    position: absolute; top: 572px; left: 38px;
    font-family: "Roboto", sans-serif; font-size: 16px; line-height: 21.8px; color: var(--ink);
  }
  .distributor strong { font-weight: 700; font-size: 18px; }
  .distributor__item { margin-top: 16px; }
  .partner {
    position: absolute; top: 648px; left: 226px; display: flex; align-items: center; gap: 6px;
    font-family: "Roboto", sans-serif; font-weight: 700; font-size: 19px; color: var(--forest);
  }
  .partner__dot { width: 14px; height: 14px; border-radius: 50%; background: var(--forest); }
  .code-box {
    position: absolute; top: 773px; left: 62px; width: 258px; height: 97px;
    background: var(--white); border: 2px solid var(--ink);
  }
</style>
</head>
<body>
<main class="sheet">

  <section class="label label--front" aria-label="Front label">
    <div class="brand">VARUMEK</div>
    <h1 class="title title__main">ALOE VERA</h1>
    <div class="title title__sub">GEL</div>
    <div class="plant" role="img" aria-label="Photo of an aloe vera plant reflected in water"></div>
    <div class="tagline">Non Oily</div>
    <div class="rule-dashed"></div>
    <div class="natural">
      <div class="natural__pct">98%</div>
      <div class="natural__text"><b>NATURAL</b><span>ALOE VERA GEL</span></div>
    </div>
    <div class="rule-solid rule-solid--top"></div>
    <div class="band">
      <p class="band__text">Skin Care<br>From Natures<br>Wonder Plant</p>
    </div>
    <div class="plant" role="img" aria-label="Photo of an aloe vera plant reflected in water"></div>
    <div class="rule-solid rule-solid--bottom"></div>
    <div class="volume">250ml</div>
  </section>

  <section class="label label--rear" aria-label="Rear label">
    <div class="brand">VARUMEK</div>
    <div class="rule-dashed rule-dashed--upper"></div>
    <h2 class="heading-box">ALOE VERA GEL</h2>
    <div class="heading-box heading-box--under"></div>
    <p class="about">Aloe Vera is a natural substance<br>derived from the sap of the Aloe<br>Vera plant. Use Aloe Vera Gel for<br>the relief of sunburn , minor cuts<br>and burns and dry skins.</p>
    <h3 class="ingredients-tag">INGREDIENTS</h3>
    <p class="ingredients">Water (Aqua), Alcohol, Glycerin, Aloe<br>Barbadensis Leaf Extract, PEG-40<br>Hydrogenated Castor Oil, Phenoxyeth-<br>anol, Propylene Glycol, Diazolidinyl<br>Urea, Iodopropynyl Butylcarbamate,<br>Carbomer, Triethanolamine, Fragrance,<br>Yellow 5 CI19140, Blue 1 CI42090.</p>
    <div class="rule-dashed rule-dashed--lower"></div>
    <div class="distributor">
      <p>DISTRIBUTED BY<br><strong>Nordlane Pty Limited</strong><br>18-20 MERRIN STREET<br>KELLOWAY NSW 2301<br>Made in Austrlia<br>www.nordlane.com.au</p>
      <p class="distributor__item">Item No: AV208</p>
    </div>
    <div class="partner"><span class="partner__dot"></span>NORDLANE</div>
    <div class="code-box"></div>
  </section>

</main>
</body>
</html>
```